Artificial intelligence, machine learning, and automation company needs a sexy business card design

We need a sleek and sexy business card design for an AI consulting company based in Philadelphia PA. We provide custom machine learning and automation solutions for companies of all shapes and sizes. The primary industries that we serve are pharmaceuticals, engineering, healthcare, and computer software. We would like the designs to be a black business card that uses green as a sleek accent color. The final design should communicate intelligence, cutting edge new-tech, and optimization.

Target Market(s)

C-level and VP level executives of multi-million annual companies. Mostly in Pharma, Healthcare, Real Estate, Retail, and Engineering

Industry/Entity Type

Computer Software

Contact Information for Business Card

Name: Jack Moss
Title: CEO
Cell: 215 604 8293
Email: JackM@quillarcworks.example
Website: www.QuillarcWorks.example

Font styles to use
Sans Serif

Colors

Designer to choose colors to be used in the design.

Requirements
Must have
• 1) Attached Quillarc Logo (either with colors or not/embossed)
• 2) "Artificial Intelligence" "Automation" and "Machine Learning"
• 3) "Quillarc Laboratories" or "Quillarc Works" or "Quillarc"
• 4) Sexy AF.
Nice to have
• Black card / dark card color, "Quillarc Green" accent colors (in attached .ai file), Embossment of logo/name/etc, thick card stock, colored borders (on card sides, not front/back faces)
Should not have
• Should not be bland, or unsexy.

```html
<!DOCTYPE html>
<html lang="en">
<head>
<meta charset="utf-8">
<title>Quillarc Laboratories – Business Card</title>
<link href="https://fonts.googleapis.com/css2?family=Open+Sans:wght@400;700;800&display=swap" rel="stylesheet">
<style>
  :root {
    --slate: #3a4647;
    --quillarc-green: #66ff99;
    --citron: #d4d419;
    --paper: #ffffff;
  }
  * { box-sizing: border-box; margin: 0; padding: 0; }
  html, body { width: 985px; height: 1200px; overflow: hidden; background: var(--paper); }
  body { font-family: "Open Sans", Arial, sans-serif; }
  .canvas { position: relative; width: 985px; height: 1200px; }

  /* Front face */
  .front { position: absolute; left: 0; top: 0; width: 985px; height: 579px; background: var(--paper); }
  .brand-mark { position: absolute; border: 10px solid var(--quillarc-green); background: var(--slate); }
  .front .brand-mark { left: 406px; top: 80px; width: 172px; height: 164px; border-width: 7px; }
  .brand-name { position: absolute; left: 0; width: 100%; text-align: center; font-weight: 400; line-height: 1; }
  .front .brand-name { color: var(--slate); top: 256px; font-size: 22px; letter-spacing: 5px; }
  .brand-name .sub { display: block; font-size: 0.62em; letter-spacing: 4px; margin-top: 8px; }

  .contact-band { position: absolute; left: 0; top: 357px; width: 985px; height: 222px; background: var(--slate); }
  .accent-rule { position: absolute; left: 0; width: 985px; height: 8px; background: var(--citron); }
  .accent-rule.upper { top: 22px; }
  .accent-rule.lower { top: 192px; }
  .identity { position: absolute; left: 0; top: 30px; width: 427px; height: 162px; color: var(--paper); text-align: center; }
  .identity .person { margin-top: 38px; font-size: 42px; font-weight: 800; line-height: 1; }
  .identity .role { margin-top: 18px; font-size: 32px; font-weight: 400; line-height: 1; }
  .details { position: absolute; left: 427px; top: 30px; width: 558px; height: 162px; background: var(--quillarc-green); list-style: none; }
  .details li { position: absolute; left: 62px; display: flex; align-items: center; color: var(--slate); font-size: 28px; line-height: 1; }
  .details li:nth-child(1) { top: 17px; }
  .details li:nth-child(2) { top: 64px; }
  .details li:nth-child(3) { top: 112px; }
  .details svg { width: 24px; height: 24px; margin-right: 22px; flex: none; }

  /* Back face */
  .back { position: absolute; left: 0; top: 620px; width: 985px; height: 580px; background: var(--slate); }
  .back .brand-mark { left: 356px; top: 110px; width: 273px; height: 260px; }
  .back .brand-name { color: var(--citron); top: 392px; font-size: 46px; letter-spacing: 10px; }
  .back .brand-name .sub { font-size: 0.55em; letter-spacing: 8px; margin-top: 14px; }
  .back .site { position: absolute; left: 0; width: 100%; top: 516px; text-align: center; color: var(--quillarc-green); font-size: 27px; }
</style>
</head>
<body>
<div class="canvas">
  <section class="front">
    <div class="brand-mark"></div>
    <div class="brand-name">QUILLARC<span class="sub">LABORATORIES</span></div>

    <div class="contact-band">
      <div class="accent-rule upper"></div>
      <div class="identity">
        <p class="person">Jack Moss</p>
        <p class="role">CEO</p>
      </div>
      <ul class="details">
        <li>
          <svg viewBox="0 0 24 24" aria-hidden="true"><path d="M6 3l3 4-2 2c1 2.5 3.5 5 6 6l2-2 4 3-2 4C10 19 5 14 4 5z" fill="#3a4647"/></svg>
          215 604 8293
        </li>
        <li>
          <svg viewBox="0 0 24 24" aria-hidden="true"><rect x="2" y="6" width="20" height="13" fill="#3a4647"/><path d="M2 6l10 7 10-7" fill="none" stroke="#66ff99" stroke-width="1.5"/></svg>
          JackM@quillarcworks.example
        </li>
        <li>
          <svg viewBox="0 0 24 24" aria-hidden="true" fill="none" stroke="#3a4647" stroke-width="1.5"><circle cx="12" cy="12" r="9"/><ellipse cx="12" cy="12" rx="4" ry="9"/><path d="M3 12h18M5 7.5h14M5 16.5h14"/></svg>
          www.QuillarcWorks.example
        </li>
      </ul>
      <div class="accent-rule lower"></div>
    </div>
  </section>

  <section class="back">
    <div class="brand-mark"></div>
    <div class="brand-name">QUILLARC<span class="sub">LABORATORIES</span></div>
    <p class="site">www.QuillarcWorks.example</p>
  </section>
</div>
</body>
</html>
```